Design a Brazilian children's Bible calendar for 2017

We need someone to design a children's calendar for 2017 with an animal theme.
The format is 21cm x 15cm and we need the front cover and one page with two months as can be seen in the attached files.
Target Market(s)
Brazilian children
Font styles to use
Sans Serif
Requirements
Must have
- Modern, clean design

```html
<!DOCTYPE html>
<html lang="pt-BR">
<head>
<meta charset="utf-8">
<title>Calendário Infantil 2017 — Março e Abril</title>
<link href="https://fonts.googleapis.com/css2?family=Open+Sans:wght@400;600&family=Arimo:wght@400;700&display=swap" rel="stylesheet">
<style>
  :root {
    --page-pink: #f6c9cf;
    --page-pink-light: #fbe0e3;
    --photo-green-dark: #2f4a1c;
    --photo-green: #6b8f3a;
    --verse-green: #9fcb3a;
    --verse-text: #1f3d6b;
    --header-band: #f3ef8e;
    --header-red: #d9262b;
    --dayname-band: #f7f39b;
    --cell-border: #d9262b;
    --cell-bg: #ffffff;
    --weekend-bg: #eeeeee;
    --number: #1a1a1a;
    --footer-green: #9fcb3a;
  }
  * { margin: 0; padding: 0; box-sizing: border-box; }
  html, body { width: 857px; height: 1200px; overflow: hidden; }
  body {
    background: #ffffff;
    font-family: "Arimo", Arial, sans-serif;
  }
  .calendar-page {
    position: relative;
    width: 857px;
    height: 1200px;
    background: var(--page-pink);
    overflow: hidden;
  }
  .hero-photo {
    position: absolute;
    left: 0; top: 0;
    width: 857px; height: 614px;
    background: linear-gradient(180deg, var(--photo-green-dark) 0%, #3c5a22 45%, var(--photo-green) 100%);
  }
  .verse-box {
    position: absolute;
    left: 220px; top: 634px;
    width: 488px; height: 118px;
    background: var(--verse-green);
    border-radius: 6px;
    text-align: center;
    color: var(--verse-text);
    padding-top: 12px;
  }
  .verse-text {
    font-family: "Open Sans", Arial, sans-serif;
    font-size: 30px;
    line-height: 32px;
  }
  .verse-ref {
    position: absolute;
    right: 14px; bottom: 10px;
    font-family: "Open Sans", Arial, sans-serif;
    font-size: 14px;
  }
  .month {
    position: absolute;
    top: 777px;
    width: 388px;
    height: 356px;
    background: var(--page-pink-light);
  }
  .month--march { left: 36px; }
  .month--april { left: 446px; }
  .month-header {
    height: 46px;
    background: var(--header-band);
    display: flex;
    justify-content: space-between;
    align-items: center;
    padding: 0 16px 0 40px;
    color: var(--header-red);
    font-weight: 700;
    font-size: 29px;
  }
  .day-names {
    display: grid;
    grid-template-columns: repeat(7, 1fr);
    height: 34px;
    background: var(--dayname-band);
    align-items: center;
    text-align: center;
    font-weight: 700;
    font-size: 17px;
    color: var(--number);
    padding: 0 6px;
  }
  .days {
    display: grid;
    grid-template-columns: repeat(7, 1fr);
    grid-auto-rows: 51px;
    gap: 3px;
    padding: 6px 8px;
  }
  .day {
    background: var(--cell-bg);
    border: 2px solid var(--cell-border);
    display: flex;
    align-items: center;
    justify-content: center;
    font-weight: 700;
    font-size: 24px;
    color: var(--number);
  }
  .day--weekend { background: var(--weekend-bg); }
  .page-footer {
    position: absolute;
    left: 0; bottom: 38px;
    width: 857px; height: 8px;
    background: var(--footer-green);
  }
</style>
</head>
<body>
<main class="calendar-page">
  <div class="hero-photo" role="img" aria-label="Fotografia de um filhote de cachorro claro sentado na grama ao lado de um gatinho rajado"></div>

  <section class="verse-box">
    <p class="verse-text">No principio, criou<br>Deus os ceus<br>e a terra.</p>
    <span class="verse-ref">Genesis 1 v 1</span>
  </section>

  <section class="month month--march">
    <header class="month-header"><span>Marcha</span><span>2017</span></header>
    <div class="day-names"><span>Dom</span><span>Seg</span><span>Ter</span><span>Qua</span><span>Qui</span><span>Sex</span><span>Sáb</span></div>
    <div class="days">
      <div class="day day--weekend"></div><div class="day"></div><div class="day"></div><div class="day">1</div><div class="day">2</div><div class="day">3</div><div class="day day--weekend">4</div>
      <div class="day day--weekend">5</div><div class="day">6</div><div class="day">7</div><div class="day">8</div><div class="day">9</div><div class="day">10</div><div class="day day--weekend">11</div>
      <div class="day day--weekend">12</div><div class="day">13</div><div class="day">14</div><div class="day">15</div><div class="day">16</div><div class="day">17</div><div class="day day--weekend">18</div>
      <div class="day day--weekend">19</div><div class="day">20</div><div class="day">21</div><div class="day">22</div><div class="day">23</div><div class="day">24</div><div class="day day--weekend">25</div>
      <div class="day day--weekend">26</div><div class="day">27</div><div class="day">28</div><div class="day">29</div><div class="day">30</div><div class="day">31</div><div class="day day--weekend"></div>
    </div>
  </section>

  <section class="month month--april">
    <header class="month-header"><span>Abril</span><span>2017</span></header>
    <div class="day-names"><span>Dom</span><span>Seg</span><span>Ter</span><span>Qua</span><span>Qui</span><span>Sex</span><span>Sáb</span></div>
    <div class="days">
      <div class="day day--weekend">30</div><div class="day"></div><div class="day"></div><div class="day"></div><div class="day"></div><div class="day"></div><div class="day day--weekend">1</div>
      <div class="day day--weekend">2</div><div class="day">3</div><div class="day">4</div><div class="day">5</div><div class="day">6</div><div class="day">7</div><div class="day day--weekend">8</div>
      <div class="day day--weekend">9</div><div class="day">10</div><div class="day">11</div><div class="day">12</div><div class="day">13</div><div class="day">14</div><div class="day day--weekend">15</div>
      <div class="day day--weekend">16</div><div class="day">17</div><div class="day">18</div><div class="day">19</div><div class="day">20</div><div class="day">21</div><div class="day day--weekend">22</div>
      <div class="day day--weekend">23</div><div class="day">24</div><div class="day">25</div><div class="day">26</div><div class="day">27</div><div class="day">28</div><div class="day day--weekend">29</div>
    </div>
  </section>

  <div class="page-footer"></div>
</main>
</body>
</html>
```